Web Design Project - Quiet Harbor Advisors

I have a requirement for a simple website that I can manage and change content myself. I'd like to be able to include and change images frequently.

I run a small consulting firm and focus on the area of small to medium sized business turn around. The premise of the business service is that most small businesses "have a monkey on their back" - a problem they need to solve - for example "a Sales Monkey" where their sales team didn't have a solid process or approach or training or the right people; or "a Finance Monkey" where they needed help with Cash flow management or funding, or "an IT Monkey" where their IT systems aren't supporting their supply chain process or ordering process.

So the whole business is build around building monkey characters to represent specific business problems - thus the name Quiet Harbor Advisors.

This always builds into giving each employee their own Monkey character - mine is an Orangutan and appears on my card and Deon (who is our Lawyer) is a Baboon and his character is on his card. I'd like to see these characters also integrated into the site.

The site need to be pretty simple at this stage:

1. Home Page
2. Services Page
3. Who we are / team page
4. Contact Us page

Due to the nature of the name and the imagery around the business I'd like the site to be engaging and colourful, the language I'll use is accessible, down to earth and customer/solution focused.

Target Market(s)

Small to medium sized enterprises looking for assistance with their business. They will be looking for practical solutions at value for money pricing

Industry/Entity Type

Business Service

Requirements
Nice to have
• I'd like the monkey in the logo to swing.

On the People or team page - each person is to have their own monkey character - for example - my business card shows my monkey character as an Orangutan and Deon's monkey character is a baboon - so as the business grows each new person gets their own monkeys character. So on the people or team page it would be fun to have some kind of jungle scene with the character monkeys placed in there and some descriptor of the person.

```html
<!DOCTYPE html>
<html lang="en">
<head>
<meta charset="utf-8">
<title>Quiet Harbor Advisors</title>
<link rel="stylesheet" href="https://fonts.googleapis.com/css2?family=Arvo:wght@400;700&family=Ubuntu:wght@400;500&display=swap">
<style>
  :root{
    --page-bg:#ebebeb;
    --hero-side:#c9b000;
    --hero:#dcc300;
    --hero-art:#e3cc24;
    --brown:#6e4410;
    --brown-dark:#5a360a;
    --btn-top:#a5600f;
    --btn-bottom:#7a430a;
    --pill-top:#f6e64a;
    --pill-bottom:#d8c000;
    --pill-edge:#b49d00;
    --ink:#3a3a3a;
    --body:#444;
    --icon:#9a9a9a;
    --rule:#e2e2e2;
    --white:#fff;
  }
  *{box-sizing:border-box;margin:0;padding:0}
  html,body{width:1054px;height:1200px;overflow:hidden}
  body{background:var(--page-bg);font-family:"Ubuntu",sans-serif;color:var(--body);position:relative}
  .hero-band{position:absolute;left:0;top:0;width:1054px;height:456px;background:var(--hero-side)}
  .hero{position:absolute;left:70px;top:0;width:914px;height:456px;background:var(--hero);overflow:hidden}
  .hero-art{position:absolute;left:465px;top:95px;width:400px;height:361px;border-radius:200px 200px 0 0;
    background:radial-gradient(ellipse at 50% 40%,var(--hero-art),var(--hero) 72%)}
  .nav{position:absolute;left:55px;top:37px;width:804px;height:55px;background:var(--white);
    border-bottom:3px solid var(--pill-bottom);display:flex;align-items:center}
  .brand{width:268px;padding-left:14px;font-size:19px;color:var(--brown);letter-spacing:.5px;border-right:1px solid var(--rule);height:100%;display:flex;align-items:center}
  .menu{display:flex;height:100%;list-style:none}
  .menu li{display:flex;align-items:center;padding:0 20px;font-size:12px;color:#555;border-right:1px solid var(--rule)}
  .menu li.active{color:var(--brown);font-weight:500}
  .social{display:flex;gap:10px;padding-left:14px}
  .social span{width:20px;height:20px;background:var(--brown);border-radius:3px}
  .hero-lead{position:absolute;left:75px;top:132px;font-family:"Arvo",serif;font-size:27px;line-height:34px;color:var(--brown);white-space:nowrap}
  .hero-title{position:absolute;left:75px;top:170px;font-family:"Arvo",serif;font-weight:700;font-size:24px;line-height:36px;color:var(--brown);white-space:nowrap}
  .hero-text{position:absolute;left:75px;top:278px;width:350px;font-size:11px;line-height:14px;color:var(--brown)}
  .cta{position:absolute;left:72px;top:373px;width:226px;height:43px;border-radius:22px;
    background:linear-gradient(var(--btn-top),var(--btn-bottom));border:2px solid var(--brown-dark);
    color:var(--white);font-family:"Arvo",serif;font-weight:700;font-size:17px;display:flex;align-items:center;justify-content:center}
  .main{position:absolute;left:70px;top:456px;width:914px;height:705px;background:var(--white)}
  .services{display:flex;height:268px;border-bottom:1px solid var(--rule)}
  .service{flex:1;text-align:center;padding-top:36px}
  .service h2{font-size:18px;font-weight:500;color:var(--ink)}
  .service svg{display:block;margin:12px auto 0}
  .service h3{font-family:"Arvo",serif;font-weight:400;font-size:18px;color:var(--ink);margin-top:20px}
  .service p{font-size:10.5px;line-height:13px;width:190px;margin:7px auto 0}
  .pill{display:inline-flex;align-items:center;justify-content:center;width:83px;height:23px;border-radius:12px;
    background:linear-gradient(var(--pill-top),var(--pill-bottom));border:1px solid var(--pill-edge);font-size:11px;color:#5a4a00;margin-top:18px}
  .why{text-align:center;height:193px;border-bottom:1px solid var(--rule);padding-top:28px}
  .why h2,.clients h2{font-size:18px;font-weight:500;color:var(--ink)}
  .why p{font-size:10.5px;line-height:15px;width:790px;margin:24px auto 0}
  .why .pill{margin-top:24px}
  .clients{position:relative;text-align:center;padding-top:28px;height:244px}
  .strip{position:absolute;left:22px;top:76px;width:873px;height:58px}
  .arrow{position:absolute;top:15px;width:18px;height:25px;background:var(--pill-bottom);border:1px solid var(--pill-edge)}
  .arrow svg{display:block;margin:8px auto}
  .arrow.prev{left:0}.arrow.next{right:0}
  .photo{position:absolute;top:0;width:57px;height:57px;border:2px solid var(--white);outline:1px solid #ddd;
    background:linear-gradient(135deg,#8a8a8a,#2e2e2e)}
  .photo.current{border-color:var(--pill-bottom);outline-color:var(--pill-edge)}
  .quote{position:absolute;left:130px;top:160px;width:660px;font-size:10.5px;line-height:15px}
  .quote cite{display:block;font-style:normal;font-weight:500;font-size:12px;color:var(--ink);margin-top:9px}
  .footer{position:absolute;left:0;top:1173px;width:1054px;text-align:center;font-size:11px;color:#555}
</style>
</head>
<body>
  <div class="hero-band"></div>
  <header class="hero">
    <div class="hero-art" role="img" aria-label="Faint outline of the cheerful mascot waving"></div>
    <nav class="nav">
      <div class="brand">quiet harbor advisors</div>
      <ul class="menu">
        <li class="active">Home</li>
        <li>Services</li>
        <li>Who we are / team page</li>
        <li>Contact Us</li>
      </ul>
      <div class="social"><span></span><span></span><span></span></div>
    </nav>
    <p class="hero-lead">you have monkey on your back</p>
    <h1 class="hero-title">Your any problem will be<br>Solved here!</h1>
    <p class="hero-text">Ut wisi enim ad minim veniam, quis nostrud exerci tation ullamcorper suscipit lobortis nisl ut aliquip ex ea commodo consequat. Duis autem vel eum iriure dolor ...</p>
    <div class="cta">Let us help you!</div>
  </header>

  <main class="main">
    <section class="services">
      <div class="service">
        <h2>Sales Monkey?</h2>
        <svg width="62" height="62" viewBox="0 0 62 62" aria-hidden="true">
          <circle cx="30" cy="32" r="28" fill="none" stroke="var(--icon)" stroke-width="3"/>
          <path d="M33 1 A28 28 0 0 1 61 29 L33 29 Z" fill="var(--icon)"/>
        </svg>
        <h3>liber tempor</h3>
        <p>lectorum. Mirum est notare quam littera gothica, quam nunc putamus</p>
        <span class="pill">More</span>
      </div>
      <div class="service">
        <h2>Finance Monkey?</h2>
        <svg width="62" height="62" viewBox="0 0 62 62" aria-hidden="true">
          <path d="M2 2 V58 H62" fill="none" stroke="var(--icon)" stroke-width="3"/>
          <rect x="8" y="2" width="10" height="52" fill="var(--icon)"/>
          <rect x="20" y="16" width="10" height="38" fill="var(--icon)"/>
          <rect x="32" y="34" width="10" height="20" fill="var(--icon)"/>
          <rect x="44" y="46" width="10" height="8" fill="var(--icon)"/>
        </svg>
        <h3>liber tempor</h3>
        <p>lectorum. Mirum est notare quam littera gothica, quam nunc putamus</p>
        <span class="pill">More</span>
      </div>
      <div class="service">
        <h2>IT Monkey?</h2>
        <svg width="62" height="62" viewBox="0 0 62 62" aria-hidden="true">
          <path d="M2 12 C8 0 24 0 34 10" fill="none" stroke="var(--icon)" stroke-width="2"/>
          <rect x="18" y="10" width="34" height="50" rx="15" fill="var(--icon)"/>
          <rect x="31" y="22" width="8" height="14" rx="4" fill="var(--white)"/>
        </svg>
        <h3>liber tempor</h3>
        <p>lectorum. Mirum est notare quam littera gothica, quam nunc putamus</p>
        <span class="pill">More</span>
      </div>
    </section>

    <section class="why">
      <h2>Why choose us?</h2>
      <p>Ut wisi enim ad minim veniam, quis nostrud exerci tation ullamcorper suscipit lobortis nisl ut aliquip ex ea commodo consequat. Duis autem vel eum iriure dolor in hendrerit in vulputate velit esse molestie consequat, vel illum dolore eu feugiat nulla facilisis at vero eros et accumsan et iusto odio dignissim qui blandit praesent luptatum zzril delenit augue duis dolore te feugait nulla facilisi. Nam liber tempor cum soluta nobis eleifend ...</p>
      <span class="pill">More</span>
    </section>

    <section class="clients">
      <h2>Happy Clients</h2>
      <div class="strip">
        <div class="arrow prev"><svg width="6" height="8" viewBox="0 0 6 8"><path d="M6 0 L0 4 L6 8Z" fill="#333"/></svg></div>
        <div class="photo" style="left:35px" role="img" aria-label="Client portrait"></div>
        <div class="photo" style="left:103px" role="img" aria-label="Client portrait"></div>
        <div class="photo" style="left:171px" role="img" aria-label="Client portrait"></div>
        <div class="photo" style="left:239px" role="img" aria-label="Client portrait"></div>
        <div class="photo" style="left:307px" role="img" aria-label="Client portrait"></div>
        <div class="photo" style="left:375px" role="img" aria-label="Client portrait"></div>
        <div class="photo" style="left:443px" role="img" aria-label="Client portrait"></div>
        <div class="photo current" style="left:511px" role="img" aria-label="Selected client portrait"></div>
        <div class="photo" style="left:579px" role="img" aria-label="Client portrait"></div>
        <div class="photo" style="left:647px" role="img" aria-label="Client portrait"></div>
        <div class="photo" style="left:715px" role="img" aria-label="Client portrait"></div>
        <div class="photo" style="left:783px" role="img" aria-label="Client portrait"></div>
        <div class="arrow next"><svg width="6" height="8" viewBox="0 0 6 8"><path d="M0 0 L6 4 L0 8Z" fill="#333"/></svg></div>
      </div>
      <blockquote class="quote">
        <p>“ Ut wisi enim ad minim veniam, quis nostrud exerci tation ullamcorper suscipit lobortis nisl ut aliquip ex ea commodo consequat. Duis autem vel eum iriure dolor in hendrerit in vulputate velit esse molestie consequat, vel illum dolore eu feugiat nulla facilisis ”</p>
        <cite>-Lena Ortiz</cite>
      </blockquote>
    </section>
  </main>

  <footer class="footer">Copyright © 2013 quiet harbor advisors.</footer>
</body>
</html>
```